Bref créative
Law firm stationary package
Letterhead, business card, envelope
Professional
Theodore R. Wexley
Attorney at Law
5183 Poldin Lane, Suite A
P.O. Box 81947
Cincinnati, OH 45867
Ted@WexleyCounsel.example
www.WexleyCounsel.example
Please create business card, letterhead, and envelope designs.
Focus on clean, professional design for this corporate law firm. Stay away from watermarks, waves, or anything that is too ink-intensive. You may use either or both of the attached logos.
Main logo
Inverse of logo, use is optional

```html
<!DOCTYPE html>
<html lang="en">
<head>
<meta charset="utf-8">
<title>Wexley Counsel – Business Card</title>
<link href="https://fonts.googleapis.com/css2?family=Tinos:wght@400;700&display=swap" rel="stylesheet">
<style>
  :root{
    --bg:#e4e4e6;
    --card:#ffffff;
    --navy:#312d7c;
    --gray:#8d8d8f;
    --light:#efeff1;
    --ink:#2b2b2f;
    --rule:#b9b9bd;
  }
  html,body{margin:0;padding:0;overflow:hidden}
  body{width:1200px;height:901px;background:var(--bg);font-family:"Tinos","Times New Roman",serif;color:var(--ink);position:relative}
  .card{position:absolute;left:250px;width:700px;height:400px;background:var(--card);box-shadow:0 6px 18px rgba(0,0,0,.18);overflow:hidden}
  .card-back{top:30px}
  .card-front{top:470px}

  .brand{position:absolute;display:flex;align-items:center;gap:16px}
  .brand-square{width:46px;height:46px;background:var(--navy);border-radius:6px}
  .brand-name{font-size:40px;color:var(--navy);letter-spacing:1px;white-space:nowrap}

  .card-back .brand{left:50%;top:150px;transform:translateX(-50%)}
  .card-back .brand-square{width:70px;height:70px;border-radius:10px}
  .card-back .brand-name{font-size:44px}
  .back-web{position:absolute;left:0;right:0;top:250px;text-align:center;font-size:17px;letter-spacing:4px;color:var(--gray)}

  .card-front .brand{left:120px;top:52px}
  .brand-rule{position:absolute;left:196px;top:118px;width:330px;height:1px;background:var(--navy)}

  .gray-tab{position:absolute;left:0;top:208px;width:180px;height:26px;background:var(--gray)}
  .navy-band{position:absolute;left:0;top:208px;width:700px;height:60px}
  .holder{position:absolute;right:40px;top:175px;text-align:right}
  .holder-name{font-size:24px;font-weight:700;color:var(--navy)}
  .holder-title{font-size:16px;margin-top:2px}
  .band-web{position:absolute;left:280px;top:244px;font-size:16px;letter-spacing:5px;color:#fff}

  .details{position:absolute;left:0;top:268px;width:700px;height:132px;background:var(--light);display:flex}
  .col{padding:22px 0 0 22px;font-size:17px;line-height:1.3}
  .col-address{width:230px}
  .col-phones,.col-direct{border-left:1px solid var(--rule);padding-top:30px}
  .col-phones{width:160px}
  .line{display:flex;align-items:center;gap:10px}
  .icon{width:18px;height:18px;fill:var(--ink);flex:none}
</style>
</head>
<body>

<section class="card card-back">
  <div class="brand">
    <span class="brand-square"></span>
    <span class="brand-name">Wexley Counsel, LLC</span>
  </div>
  <div class="back-web">www.WexleyCounsel.example</div>
</section>

<section class="card card-front">
  <div class="brand">
    <span class="brand-square"></span>
    <span class="brand-name">Wexley Counsel, LLC</span>
  </div>
  <div class="brand-rule"></div>

  <div class="gray-tab"></div>
  <svg class="navy-band" viewBox="0 0 700 60" aria-hidden="true">
    <polygon points="250,26 700,26 700,60 250,60" fill="var(--navy)"/>
    <polygon points="180,0 230,0 270,60 220,60" fill="var(--card)"/>
  </svg>

  <div class="holder">
    <div class="holder-name">Theodore R. Wexley</div>
    <div class="holder-title">Attorney at Law</div>
  </div>
  <div class="band-web">www.WexleyCounsel.example</div>

  <div class="details">
    <div class="col col-address">
      5183 Poldin Lane, Suite A<br>
      P.O. Box 81947<br>
      Cincinnati, OH 45867
    </div>
    <div class="col col-phones">
      <div class="line">
        <svg class="icon" viewBox="0 0 24 24" aria-hidden="true"><path d="M6.6 10.8a15 15 0 0 0 6.6 6.6l2.2-2.2a1 1 0 0 1 1-.25 11.4 11.4 0 0 0 3.6.57 1 1 0 0 1 1 1V20a1 1 0 0 1-1 1A17 17 0 0 1 3 4a1 1 0 0 1 1-1h3.5a1 1 0 0 1 1 1c0 1.25.2 2.45.57 3.6a1 1 0 0 1-.25 1z"/></svg>
        <span>888.555.0142<br>513.555.0187</span>
      </div>
    </div>
    <div class="col col-direct">
      <div class="line">
        <svg class="icon" viewBox="0 0 24 24" aria-hidden="true"><path d="M6 2h9v6H6zM4 9h16a2 2 0 0 1 2 2v9H2v-9a2 2 0 0 1 2-2zm2 4v2h3v-2zm5 0v2h3v-2z"/></svg>
        <span>513.555.0163</span>
      </div>
      <div class="line">
        <svg class="icon" viewBox="0 0 24 24" aria-hidden="true"><path d="M2 5h20v14H2zm2 2v.5l8 5 8-5V7zm0 2.8V17h16V9.8l-8 5z"/></svg>
        <span>Ted@WexleyCounsel.example</span>
      </div>
    </div>
  </div>
</section>

</body>
</html>
```